We need a new menu with more professional outlook for our restaurant called Mei Tan Garden Vegetarian Cuisine. We are vegetarian restaurant offered healthy food with nice environment and service. Our restaurant's pictures and take away menu are available on www.meitan-eatery.com.au. I want to redesign our eat in and take away menu to be similar to our restaurant's theme and something which is green, healthy and professional. I gave the menu of my favorite restaurant on Google Docs.
Updates
Dear all,
Industry/Entity Type
Environment
Requirements
Must have
- I am really interested in the design and layout of the restaurant in our local area- please refer to these files: https://files.example-share.net/open?id=7Q-KpzeWTrmLhQaTnfXo4PvNkRsE and https://files.example-share.net/open?id=7Q-KpzeWTrmLhBvR9WcXa2LqMhT . We would like something look like this: simple, easy to follow and professional.

```html
<!DOCTYPE html>
<html lang="en">
<head>
<meta charset="utf-8">
<title>Mei Tan Garden Vegetarian Cuisine – Take-out Menu</title>
<link rel="stylesheet" href="https://fonts.googleapis.com/css2?family=Cinzel:wght@700&family=Roboto+Condensed:wght@400;700&display=swap">
<style>
:root{
  --bg:#4b4f33;
  --bg-deep:#33361f;
  --panel:rgba(44,48,28,.8);
  --panel-edge:rgba(150,160,90,.45);
  --brand-panel:rgba(40,44,26,.94);
  --gold:#ebb63a;
  --gold-soft:#f2d16b;
  --desc:#d6c47c;
  --text:#f4f1e6;
  --tag:#3a4124;
  --tag-edge:#7c8c3e;
  --green:#8fb23a;
  --green-soft:#b5cf5a;
}
*{box-sizing:border-box;margin:0;padding:0}
html,body{width:848px;height:1200px;overflow:hidden}
body{
  background:radial-gradient(ellipse at 40% 30%,#60653f 0%,var(--bg) 45%,var(--bg-deep) 100%);
  font-family:"Roboto Condensed",Arial,sans-serif;
  color:var(--text);
  position:relative;
}
.panel{position:absolute;background:var(--panel);border:1px solid var(--panel-edge);padding:5px 8px;overflow:hidden}
.section-title{
  font-family:"Cinzel",Georgia,serif;font-weight:700;color:var(--gold);
  text-align:center;font-size:15px;letter-spacing:.5px;line-height:1;margin:5px 0 4px;
  padding-bottom:3px;border-bottom:1px solid rgba(143,178,58,.35);
}
.menu-list{list-style:none}
.menu-item{font-size:7.2px;line-height:1.15;margin-bottom:1.8px}
.menu-item .row{display:flex;justify-content:space-between;gap:6px;text-transform:uppercase}
.menu-item .price{color:var(--gold-soft);white-space:nowrap}
.menu-item .desc{display:block;color:var(--desc);font-size:6px;line-height:1.12;text-transform:none}
.note{font-size:6.8px;color:var(--gold-soft);line-height:1.25;text-transform:uppercase;margin:2px 0}

.mains{left:6px;top:6px;width:316px;height:558px}
.drinks{left:329px;top:6px;width:244px;height:558px}
.brand{left:580px;top:6px;width:262px;height:558px;background:var(--brand-panel);padding:0}
.starters{left:6px;top:574px;width:316px;height:478px}
.noodles{left:329px;top:574px;width:244px;height:478px}
.specials{left:580px;top:574px;width:262px;height:620px}

.dessert-wrap{display:flex;gap:6px}
.dessert-wrap .menu-list{flex:1}
.dessert-photo{width:52px;height:46px;margin-top:30px;background:linear-gradient(135deg,#e8dcc0,#8a6a3c 60%,#3b2c1e);flex:none}

.banquet-cols{display:flex;justify-content:space-between;gap:8px;font-size:6.4px;line-height:1.28;text-transform:uppercase}
.banquet-cols .price{color:var(--gold-soft)}

.brand-mark{height:190px;display:flex;flex-direction:column;align-items:center;justify-content:center;gap:8px;padding-top:20px}
.brand-mark .dot{width:34px;height:34px;border-radius:50%;background:var(--green)}
.brand-name{font-family:"Cinzel",Georgia,serif;font-weight:700;color:var(--gold);font-size:15px;text-align:center;line-height:1.25;padding:0 16px}
.menu-title{font-family:"Cinzel",Georgia,serif;font-weight:700;color:var(--gold-soft);text-align:center;font-size:22px;line-height:1.15;margin-top:26px}
.tags{display:grid;grid-template-columns:repeat(3,1fr);gap:6px 5px;margin:22px 10px 0}
.tag{background:var(--tag);border:1px solid var(--tag-edge);font-size:7.2px;text-align:center;padding:4px 0;color:var(--text)}
.intro{font-size:6.8px;line-height:1.3;text-align:center;margin:14px 14px 0;color:var(--text)}
.intro .warn{color:var(--green-soft)}
.info{display:flex;justify-content:space-between;margin:14px 14px 0;font-size:7px;line-height:1.3}
.info h3{font-weight:400;color:var(--green-soft);font-size:7.6px}
.info .closed{color:var(--gold-soft);margin-top:12px}

.photo-strip{position:absolute;left:6px;top:1058px;width:567px;height:136px;display:flex}
.photo{flex:1;position:relative;border-right:1px solid #222}
.photo span{position:absolute;bottom:6px;left:0;right:0;text-align:center;font-size:8px;color:#fff}
.photo.cannelloni{background:linear-gradient(160deg,#d9d2bd,#8c7c5a 60%,#3e3627)}
.photo.paw-paw{background:linear-gradient(160deg,#c9cf8a,#7b8a3a 55%,#3a3a24)}
.photo.dry-noodle{background:linear-gradient(160deg,#e0b96a,#a8662c 55%,#4a2c18)}
.photo.sweet-sour{background:linear-gradient(160deg,#d9a35a,#9b4a22 55%,#402117)}
.photo.roast-duck{background:linear-gradient(160deg,#c47a3c,#7a3a1c 55%,#2e1a12)}
</style>
</head>
<body>

<section class="panel mains">
  <h2 class="section-title">Soy Fish</h2>
  <ul class="menu-list">
    <li class="menu-item"><div class="row"><span>Fried Soy Fish with Savoury Ginger Sauce – Ca Gung</span><span class="price">$15.90</span></div><span class="desc">Crispy soy fish with ginger, onion and shallot sauce</span></li>
    <li class="menu-item"><div class="row"><span>Soy Fish in Clay Pot Sensation – Ca Kho To</span><span class="price">$15.90</span></div><span class="desc">Onions, capsicum and chilli braised in a clay pot</span></li>
    <li class="menu-item"><div class="row"><span>Soy Fish with Lemongrass – Ca Chien Xa Ot</span><span class="price">$15.90</span></div><span class="desc">Tossed with chilli, lemongrass and onions</span></li>
    <li class="menu-item"><div class="row"><span>Savoury Sweet &amp; Sour Soy Fish – Ca Xot Chua Ngot</span><span class="price">$15.90</span></div><span class="desc">Tomato, pineapple, onions, carrots and cucumbers</span></li>
    <li class="menu-item"><div class="row"><span>Soy Fish with Tamarind Sauce – Ca Xot Me</span><span class="price">$15.90</span></div></li>
  </ul>
  <h2 class="section-title">Soy Chicken</h2>
  <ul class="menu-list">
    <li class="menu-item"><div class="row"><span>Honey Roast Soy Chicken – Ga Mat Ong</span><span class="price">$15.90</span></div><span class="desc">Crispy soy chicken drizzled in honey sauce</span></li>
    <li class="menu-item"><div class="row"><span>Soy Chicken and Cashew Nut – Ga Hot Dieu</span><span class="price">$15.90</span></div><span class="desc">A mixture of fresh vegetables tossed in light sauce with cashew nuts</span></li>
    <li class="menu-item"><div class="row"><span>Lemon Grass Soy Chicken (Spicy) – Ga Xa Ot (Cay)</span><span class="price">$15.90</span></div><span class="desc">Minced lemongrass and chilli with onions and capsicum</span></li>
    <li class="menu-item"><div class="row"><span>Ginger Soy Chicken – Ga Gung</span><span class="price">$15.90</span></div><span class="desc">Thin ginger strips fried with onions, capsicum and salad</span></li>
    <li class="menu-item"><div class="row"><span>Soy Chicken Curry &amp; Veggie with Coconut Cream –</span><span class="price">$15.90</span></div><span class="desc">Coconut cream sauce with cauliflower, carrots and broccoli</span></li>
    <li class="menu-item"><div class="row"><span>Soy Chicken with Basil Leave – Ga La Que</span><span class="price">$15.90</span></div><span class="desc">A combination of vegetables and basil tossed with special sauce</span></li>
    <li class="menu-item"><div class="row"><span>Soy Chicken Satay Sauce (Spicy) – Ga Xao Sate (Cay)</span><span class="price">$15.90</span></div><span class="desc">Satay sauce with capsicum, carrots, broccoli and celery</span></li>
    <li class="menu-item"><div class="row"><span>Lemon Soy Chicken – Ga Chanh</span><span class="price">$15.90</span></div><span class="desc">Crispy soy chicken drizzled in lemon sauce</span></li>
    <li class="menu-item"><div class="row"><span>Soy Chicken on Hot Plate – Ga Vi Sat</span><span class="price">$15.90</span></div><span class="desc">Served sizzling with onions, capsicum and garlic sauce</span></li>
    <li class="menu-item"><div class="row"><span>Shanton Chicken – Ga Shanton</span><span class="price">$15.90</span></div><span class="desc">Crispy soy chicken drizzled in Shanton sauce</span></li>
    <li class="menu-item"><div class="row"><span>Chicken Drumstick and Bok Choy in Soy Sauce –</span><span class="price">$15.90</span></div><span class="desc">Soy chicken drumstick tossed in light sauce with steamed bok choy</span></li>
    <li class="menu-item"><div class="row"><span>Chicken in Plum Sauce – Ga Xi Muoi</span><span class="price">$15.90</span></div></li>
  </ul>
  <h2 class="section-title">Tofu Delight</h2>
  <ul class="menu-list">
    <li class="menu-item"><div class="row"><span>Braised Tofu and Veggie – Dau Hu Xao Rau</span><span class="price">$14.90</span></div><span class="desc">Freshly prepared vegetables tossed in our special sauce</span></li>
    <li class="menu-item"><div class="row"><span>Stuffed Beancurd in Delight Sweet &amp; Sour Sauce –</span><span class="price">$14.90</span></div><span class="desc">Tomato and lemon sauce with pineapple, onions and cucumbers</span></li>
    <li class="menu-item"><div class="row"><span>Tofu with Lemon Grass (Spicy) – Dau Hu Xa Ot (Cay)</span><span class="price">$14.90</span></div><span class="desc">Onions and capsicum tossed with minced lemongrass and chilli</span></li>
    <li class="menu-item"><div class="row"><span>Tofu with Satay Sauce (Spicy) – Dau Hu Xao Satay</span><span class="price">$14.90</span></div><span class="desc">Satay sauce with spices, cauliflower, carrots and celery</span></li>
    <li class="menu-item"><div class="row"><span>Braised Tofu and Vegetable with Cashew Nut –</span><span class="price">$15.90</span></div><span class="desc">A mixture of fresh vegetables tossed in light sauce with cashews</span></li>
  </ul>
  <h2 class="section-title">Rice</h2>
  <ul class="menu-list">
    <li class="menu-item"><div class="row"><span>Rice &amp; Veggie Combination – Com Xao Rau Cai</span><span class="price">$12.00</span></div></li>
    <li class="menu-item"><div class="row"><span>Rice &amp; Satay Tofu – Com Dau Hu Sate</span><span class="price">$12.00</span></div></li>
    <li class="menu-item"><div class="row"><span>Rice &amp; Soy Tuna in Tomato Sauce – Com Tuna Sot Ca Chua</span><span class="price">$12.00</span></div></li>
    <li class="menu-item"><div class="row"><span>Small Combination Fried Rice – Com Chien Thap Cam Nho</span><span class="price">$6.90</span></div></li>
    <li class="menu-item"><div class="row"><span>Large Combination Fried Rice – Com Chien Thap Cam Lon</span><span class="price">$7.90</span></div></li>
    <li class="menu-item"><div class="row"><span>Steamed Rice (Per Person) – Com Trang (Mot Nguoi)</span><span class="price">$2.50</span></div></li>
  </ul>
</section>

<section class="panel drinks">
  <h2 class="section-title">Beverages</h2>
  <ul class="menu-list">
    <li class="menu-item"><div class="row"><span>Mixed Lotus, Seaweed (Glass) – Sam Bo Luong</span><span class="price">$4.90</span></div><span class="desc">Served with blended ice</span></li>
    <li class="menu-item"><div class="row"><span>Three Coloured Bean Drink (Glass) – Che Ba Mau</span><span class="price">$4.90</span></div><span class="desc">Served with blended ice</span></li>
    <li class="menu-item"><div class="row"><span>Fresh Orange Juice (Glass)</span><span class="price">$4.90</span></div><span class="desc">Freshly squeezed</span></li>
    <li class="menu-item"><div class="row"><span>Young Coconut Juice (Glass) – Nuoc Dua Tuoi</span><span class="price">$3.90</span></div></li>
    <li class="menu-item"><div class="row"><span>Soy Bean Drink (Glass) (Hot or Cold) – Sua Dau Nanh</span><span class="price">$3.90</span></div><span class="desc">Homemade soybean drink</span></li>
    <li class="menu-item"><div class="row"><span>Lemon Ice Tea (Glass) – Tra Da Chanh</span><span class="price">$3.90</span></div></li>
    <li class="menu-item"><div class="row"><span>Vietnamese Ice Coffee (Glass) – Ca Phe Sua Da</span><span class="price">$3.90</span></div></li>
    <li class="menu-item"><div class="row"><span>Jasmine or Green Hot Tea (Per Person) – Tra Nong</span><span class="price">$1.90</span></div></li>
    <li class="menu-item"><div class="row"><span>Lemon Lime Bitters (Glass)</span><span class="price">$3.90</span></div></li>
    <li class="menu-item"><div class="row"><span>Lemon Soda Water (Glass)</span><span class="price">$3.90</span></div></li>
    <li class="menu-item"><div class="row"><span>Apple Juice (Glass)</span><span class="price">$3.90</span></div></li>
    <li class="menu-item"><div class="row"><span>Aloe Vera Juice (Glass)</span><span class="price">$3.90</span></div></li>
    <li class="menu-item"><div class="row"><span>Soft Drink (Can)</span><span class="price">$3.20</span></div></li>
  </ul>
  <p class="note">Includes: Cola, Diet Cola, Zero Cola, Lemonade, Orange Fizz, Lemon Squash<br>We are welcome to BYO with $1 per corkage</p>
  <h2 class="section-title">Desserts</h2>
  <div class="dessert-wrap">
    <ul class="menu-list">
      <li class="menu-item"><div class="row"><span>Fresh Young Coconut Jelly</span><span class="price">$4.90</span></div></li>
      <li class="menu-item"><div class="row"><span>Deep Fried Ice Cream</span><span class="price">$6.90</span></div></li>
      <li class="menu-item"><div class="row"><span>Deep Fried Soy Ice Cream</span><span class="price">$6.90</span></div></li>
      <li class="menu-item"><div class="row"><span>Banana Cake &amp; Coconut Cream or Ice Cream</span><span class="price">$6.90</span></div></li>
      <li class="menu-item"><div class="row"><span>Banana Fritter &amp; Coconut Cream and Ice Cream</span><span class="price">$6.90</span></div></li>
      <li class="menu-item"><div class="row"><span>Caramel Flan (No Egg) &amp; Ice Cream</span><span class="price">$4.90</span></div></li>
      <li class="menu-item"><div class="row"><span>Lychee &amp; Ice Cream</span><span class="price">$4.90</span></div></li>
      <li class="menu-item"><div class="row"><span>Logan &amp; Ice Cream</span><span class="price">$4.90</span></div></li>
      <li class="menu-item"><div class="row"><span>Sundae Ice Cream</span><span class="price">$4.00</span></div></li>
    </ul>
    <div class="dessert-photo" role="img" aria-label="Photo of a plated dessert"></div>
  </div>
  <p class="note">Extras:</p>
  <ul class="menu-list">
    <li class="menu-item"><div class="row"><span>Topping with chocolate, caramel or strawberry</span><span class="price">$0.50</span></div></li>
    <li class="menu-item"><div class="row"><span>Topping with peanuts</span><span class="price">Optional</span></div></li>
  </ul>
  <p class="note">Soy ice cream alternatives available on request</p>
  <h2 class="section-title">Banquet</h2>
  <div class="banquet-cols">
    <div>
      <span class="price">$25.00 per person (Minimum 4 persons)</span><br>
      *Spring Rolls<br>*Roast Soy Duck Wrap<br>*Fresh Cold Rolls<br>*Sizzling Mongolian Soy Lamb<br>*Honey Soy Chicken<br>*Buddha's Feast<br>*Combination Fried Rice and Steamed Rice<br>*Four Season Fruits
    </div>
    <div>
      <span class="price">$27.00 per person (Minimum 4 persons)</span><br>
      *Spring Rolls<br>*Soy Chicken Satay Sticks<br>*Curry Puffs<br>*Fresh Cold Rolls<br>*Sizzling Mongolian Soy Lamb<br>*Braised Tofu and Vegetables with Cashew Nuts<br>*Egg Plant in Clay Pot<br>*Combination Fried Rice and Steamed Rice<br>*Four Season Fruits
    </div>
  </div>
</section>

<section class="panel brand">
  <div class="brand-mark">
    <span class="dot"></span>
    <span class="brand-name">Mei Tan Garden Vegetarian Cuisine</span>
  </div>
  <h1 class="menu-title">Take - out<br>Menu</h1>
  <div class="tags">
    <span class="tag">NO EGG</span>
    <span class="tag">NO MSG</span>
    <span class="tag">NO CHOLESTEROL</span>
    <span class="tag">HEALTHY/ LOW FAT</span>
    <span class="tag">TASTY</span>
  </div>
  <p class="intro">All our dishes are vegetarian and prepared fresh without eggs, wine or MSG. All vegetarian imitation "meat" dishes like beef, pork, chicken, duck, fish, squid and seafood are made out of SOYBEAN proteins. We only use Vegetable oil in our cooking.<br><span class="warn">** Gluten Free or Nut Free are available on request**</span></p>
  <div class="info">
    <div>
      <h3>Contact information</h3>
      T: 02 5550 1234<br>F: 02 5550 1234<br><br>
      <h3>Address:</h3>
      Shop 7/12 Fernleaf Street<br>MARLOW, ACT<br>Australia 2609
    </div>
    <div>
      <h3>Opening hours :</h3>
      Tuesday- Sunday lunch<br>11:30 am- 2:30 pm<br>Monday- Sunday dinner<br>5:30 pm- 10:30 pm
      <p class="closed">CLOSED CHRISTMAS</p>
    </div>
  </div>
</section>

<section class="panel starters">
  <h2 class="section-title">Appetizers</h2>
  <ul class="menu-list">
    <li class="menu-item"><div class="row"><span>Mei Tan Spring Rolls (4 Rolls) – Cha Gio Mei Tan</span><span class="price">$6.90</span></div></li>
    <li class="menu-item"><div class="row"><span>Vegetarian Spring Rolls (4 Rolls) – Cha Gio</span><span class="price">$6.90</span></div></li>
    <li class="menu-item"><div class="row"><span>Shredded Tofu Rolls (2 Rolls) – Bi Cuon</span><span class="price">$5.50</span></div></li>
    <li class="menu-item"><div class="row"><span>Fresh Cold Rolls (2 Rolls) – Goi Cuon</span><span class="price">$5.50</span></div></li>
    <li class="menu-item"><div class="row"><span>Pocket Money Bags (4 Pieces) – Tui Tien</span><span class="price">$6.90</span></div></li>
    <li class="menu-item"><div class="row"><span>Deep-Fried Wonton (5 Pieces) – Hoanh Thanh Chien</span><span class="price">$6.90</span></div></li>
    <li class="menu-item"><div class="row"><span>Soy Chicken Nuggets (8 Pieces) – Ga Chien</span><span class="price">$6.90</span></div></li>
    <li class="menu-item"><div class="row"><span>Soy Chicken Drumsticks (5 Pieces) – Dui Ga</span><span class="price">$6.90</span></div></li>
    <li class="menu-item"><div class="row"><span>Soy Chicken Satay Sticks (3 Sticks) – Ga Sa Te</span><span class="price">$6.90</span></div></li>
    <li class="menu-item"><div class="row"><span>Mushroom Fritters (5 Pieces) – Nam Lan Bot</span><span class="price">$6.90</span></div></li>
    <li class="menu-item"><div class="row"><span>Eggplant Fritters – Ca Tim Lan Bot</span><span class="price">$6.90</span></div></li>
    <li class="menu-item"><div class="row"><span>Deep-Fried Tofu – Dau Hu Chien Don</span><span class="price">$6.90</span></div></li>
    <li class="menu-item"><div class="row"><span>Soy Crabmeat Pate – Cha Cua</span><span class="price">$7.80</span></div></li>
    <li class="menu-item"><div class="row"><span>B.B.Q Soy Meat Skewer – Thit Nuong</span><span class="price">$6.90</span></div></li>
    <li class="menu-item"><div class="row"><span>Curry Puff (4 Pieces) – Banh Cari</span><span class="price">$6.90</span></div></li>
    <li class="menu-item"><div class="row"><span>Soy Shrimp on Toast (4 Pieces) – Banh Mi Chien</span><span class="price">$6.90</span></div></li>
    <li class="menu-item"><div class="row"><span>Soy Chicken Salad – Goi Ga</span><span class="price">$11.00</span></div></li>
    <li class="menu-item"><div class="row"><span>Mei Tan Special Salad – Goi Sua</span><span class="price">$11.00</span></div></li>
    <li class="menu-item"><div class="row"><span>Paw Paw Salad – Goi Du Du</span><span class="price">$11.00</span></div></li>
    <li class="menu-item"><div class="row"><span>Asparagus Soup – Sup Mang Tay</span><span class="price">$6.90</span></div></li>
    <li class="menu-item"><div class="row"><span>Corn Soup – Sup Bap</span><span class="price">$7.50</span></div></li>
    <li class="menu-item"><div class="row"><span>Wonton Soup – Hoanh Thanh Sup</span><span class="price">$7.50</span></div></li>
    <li class="menu-item"><div class="row"><span>Soy Duck Wrap (4 Pieces) – Vit Cuon</span><span class="price">$6.90</span></div></li>
    <li class="menu-item"><div class="row"><span>Veggie Dumpling – Banh Xep Chien</span><span class="price">$6.90</span></div></li>
    <li class="menu-item"><div class="row"><span>Vegetable Steamed Buns (4 Buns) – Banh Bao</span><span class="price">$6.90</span></div></li>
  </ul>
  <h2 class="section-title">Fresh Vegetables</h2>
  <ul class="menu-list">
    <li class="menu-item"><div class="row"><span>Buddha's Feast – Rau Xao Thap Cam</span><span class="price">$14.90</span></div><span class="desc">Freshly prepared vegetables lightly tossed in our special sauce</span></li>
    <li class="menu-item"><div class="row"><span>Assorted Steamed Vegetable – Rau Hap Thap Cam</span><span class="price">$14.90</span></div><span class="desc">Fresh vegetables steamed and served with mushroom sauce</span></li>
    <li class="menu-item"><div class="row"><span>Curry Vegetable with Coconut Cream – Rau Lan Chay</span><span class="price">$14.90</span></div><span class="desc">Coconut cream sauce served with cauliflower and carrots</span></li>
    <li class="menu-item"><div class="row"><span>Braised Snow Peas and Abalone Mushroom</span><span class="price">$14.90</span></div><span class="desc">A mixture of fresh vegetables, snow peas and mushroom in light sauce</span></li>
    <li class="menu-item"><div class="row"><span>Braised Green Bean and Soy Chicken – Ga Xao Dau Que</span><span class="price">$15.90</span></div><span class="desc">A mixture of fresh vegetables and green beans tossed in light sauce</span></li>
  </ul>
</section>

<section class="panel noodles">
  <h2 class="section-title">Vietnamese Noodle Specialties</h2>
  <ul class="menu-list">
    <li class="menu-item"><div class="row"><span>Mei Tan Soy Beef Soup – Pho Bo Dac Biet</span><span class="price">$12.50</span></div></li>
    <li class="menu-item"><div class="row"><span>Soy Chicken Soup – Pho Ga</span><span class="price">$12.50</span></div></li>
    <li class="menu-item"><div class="row"><span>Soy Pork Rice Noodle Soup – Hu Tieu Nuoc</span><span class="price">$12.50</span></div></li>
    <li class="menu-item"><div class="row"><span>Soy Pork Dry Rice Noodle Soup – Hu Tieu Kho</span><span class="price">$12.50</span></div><span class="desc">Served with separate bowl of soup</span></li>
    <li class="menu-item"><div class="row"><span>Soy Seafood Rice Noodle Soup – Hu Tieu Do Bien</span><span class="price">$13.50</span></div></li>
    <li class="menu-item"><div class="row"><span>Soy Chicken Yellow Noodle Soup – Mi Ga</span><span class="price">$12.50</span></div></li>
    <li class="menu-item"><div class="row"><span>Soy Duck Yellow Noodle Soup – Mi Vit</span><span class="price">$13.50</span></div></li>
    <li class="menu-item"><div class="row"><span>Wonton Yellow Noodle Soup – Hoanh Thanh Mi</span><span class="price">$12.50</span></div></li>
    <li class="menu-item"><div class="row"><span>Combination Laksa Noodle – Mi Lac Xa</span><span class="price">$13.50</span></div></li>
    <li class="menu-item"><div class="row"><span>Royal Noodle Soup (Spicy) – Bun Bo Hue (Cay)</span><span class="price">$12.50</span></div></li>
    <li class="menu-item"><div class="row"><span>Thick Starch Home Made Noodle Soup – Banh Canh</span><span class="price">$12.50</span></div></li>
    <li class="menu-item"><div class="row"><span>Rice Vermicelli with Spring Rolls – Bun Cha Gio</span><span class="price">$12.50</span></div></li>
    <li class="menu-item"><div class="row"><span>Rice Vermicelli Spring Rolls &amp; Tofu – Bun Bi Cha Gio</span><span class="price">$12.50</span></div></li>
    <li class="menu-item"><div class="row"><span>Rice Vermicelli with B.B.Q Soy Meat – Bun Thit Nuong</span><span class="price">$12.50</span></div></li>
    <li class="menu-item"><div class="row"><span>Combination Soy Meat Veggie Stir Fry Rice Noodle</span><span class="price">$14.90</span></div><span class="desc">Hu Tieu Xao Thap Cam</span></li>
    <li class="menu-item"><div class="row"><span>Combination Soy Meat Veggie Soft or Crispy Noodle</span><span class="price">$14.90</span></div><span class="desc">Mi Xao Thap Cam Don / Mem</span></li>
    <li class="menu-item"><div class="row"><span>Combination Soy Seafood Veggie Soft or Crispy Noodle</span><span class="price">$15.90</span></div><span class="desc">Mi Xao Thap Cam Do Bien Don / Mem</span></li>
  </ul>
  <h2 class="section-title">Soy Beef</h2>
  <ul class="menu-list">
    <li class="menu-item"><div class="row"><span>Soy Beef Curry &amp; Veggie with Coconut Cream –</span><span class="price">$15.90</span></div><span class="desc">Coconut cream sauce with cauliflower, carrots and celery</span></li>
    <li class="menu-item"><div class="row"><span>Soy Beef Satay Sauce (Spicy) – Bo Xao Satay</span><span class="price">$15.90</span></div><span class="desc">Authentic satay sauce with spices and broccoli</span></li>
    <li class="menu-item"><div class="row"><span>Soy Beef and Peanut – Bo Dau Phong</span><span class="price">$15.90</span></div><span class="desc">Onions, capsicum and salad stirred in a light sauce</span></li>
    <li class="menu-item"><div class="row"><span>Soy Beef and Cashew Nut – Bo Hot Dieu</span><span class="price">$15.90</span></div><span class="desc">Fresh vegetables and soy beef tossed with cashew nuts</span></li>
    <li class="menu-item"><div class="row"><span>Soy Beef on Hot Plate – Bo Vi Sat</span><span class="price">$15.90</span></div><span class="desc">Soy beef with vegetables served on a sizzling plate</span></li>
    <li class="menu-item"><div class="row"><span>Soy Beef with Black Bean Sauce</span><span class="price">$15.90</span></div><span class="desc">Soy beef tossed with onions, capsicum and salad</span></li>
    <li class="menu-item"><div class="row"><span>Soy Beef Ginger – Bo Gung</span><span class="price">$15.90</span></div><span class="desc">Thin ginger strips fried with soy beef and onions</span></li>
    <li class="menu-item"><div class="row"><span>Soy Beef Rendang – Bo Rendang</span><span class="price">$15.90</span></div><span class="desc">Authentic rendang sauce with onions and cucumber</span></li>
  </ul>
</section>

<div class="photo-strip">
  <div class="photo cannelloni" role="img" aria-label="Photo of Vietnamese cannelloni rolls"><span>Vietnamese Cannelloni</span></div>
  <div class="photo paw-paw" role="img" aria-label="Photo of paw paw salad"><span>Paw Paw Salad</span></div>
  <div class="photo dry-noodle" role="img" aria-label="Photo of soy pork dry noodle soup"><span>Soy Pork Dry Noodle Soup</span></div>
  <div class="photo sweet-sour" role="img" aria-label="Photo of sweet and sour soup"><span>Mei Tan Sweet and Sour Soup</span></div>
  <div class="photo roast-duck" role="img" aria-label="Photo of roast soy duck"><span>Roast Soy Duck</span></div>
</div>

<section class="panel specials">
  <h2 class="section-title">Chef's Special</h2>
  <ul class="menu-list">
    <li class="menu-item"><div class="row"><span>Vietnamese Cannelloni – Banh Cuon</span><span class="price">$13.90</span></div><span class="desc">Homemade rice paper roll with soy meat and mushroom, served with fried shallots</span></li>
    <li class="menu-item"><div class="row"><span>Vietnamese Crepe – Banh Xeo</span><span class="price">$15.90</span></div><span class="desc">A crispy crepe filled with vegetables, bean sprouts and soy ham</span></li>
    <li class="menu-item"><div class="row"><span>Vietnamese Vermicelli Cake and B.B.Q Soy Meat –</span><span class="price">$15.90</span></div><span class="desc">Banh Hoi Thit Nuong: served with fresh salad and special sauce</span></li>
    <li class="menu-item"><div class="row"><span>Mei Tan Broken Rice – Com Tam Bi Suon Cha</span><span class="price">$14.90</span></div><span class="desc">Steamed broken rice with soy meat pate and shredded tofu</span></li>
    <li class="menu-item"><div class="row"><span>Special Stew Soy Beef – Bo Kho</span><span class="price">$15.90</span></div></li>
    <li class="menu-item"><div class="row"><span>Small Mei Tan Sweet and Sour Soup – Canh Chua Bap Chuoi</span><span class="price">$13.90</span></div><span class="desc">Banana flower, pineapple, tomatoes, bean shoots and basil</span></li>
    <li class="menu-item"><div class="row"><span>Large Mei Tan Sweet and Sour Soup – Canh Chua Bap Chuoi</span><span class="price">$17.90</span></div><span class="desc">Banana flower, pineapple, tomatoes, bean shoots and basil</span></li>
    <li class="menu-item"><div class="row"><span>Small Soy Seafood Sweet and Sour Soup –</span><span class="price">$16.90</span></div><span class="desc">Canh Chua Do Bien Nho: soy seafood, pineapple and tomatoes</span></li>
    <li class="menu-item"><div class="row"><span>Large Soy Seafood Sweet and Sour Soup –</span><span class="price">$18.90</span></div><span class="desc">Canh Chua Do Bien Lon: soy seafood, pineapple and tomatoes</span></li>
    <li class="menu-item"><div class="row"><span>Small Soy Beef Sweet &amp; Sour Soup (Spicy) –</span><span class="price">$15.90</span></div><span class="desc">Canh Chua Thit Bo Nho: soy beef, celery and bean shoots</span></li>
    <li class="menu-item"><div class="row"><span>Large Soy Beef Sweet &amp; Sour Soup (Spicy) –</span><span class="price">$17.90</span></div><span class="desc">Canh Chua Thit Bo Lon: soy beef, celery and bean shoots</span></li>
    <li class="menu-item"><div class="row"><span>Small Stuffed Bitter Melon Soup – Canh Kho Qua Nho</span><span class="price">$14.90</span></div></li>
    <li class="menu-item"><div class="row"><span>Large Stuffed Bitter Melon Soup – Canh Kho Qua Lon</span><span class="price">$16.90</span></div></li>
    <li class="menu-item"><div class="row"><span>Sweet &amp; Sour Soy Squid – Muc Chua Ngot</span><span class="price">$15.90</span></div><span class="desc">Tomato and lemon sauce with pineapple, onions and cucumber</span></li>
    <li class="menu-item"><div class="row"><span>Chilli Soy Squid with Variety Vegetable – Muc Xao Rau</span><span class="price">$15.90</span></div><span class="desc">Freshly prepared vegetables and soy squid in our sauce</span></li>
    <li class="menu-item"><div class="row"><span>Fried Soy Squid with Spicy Salt &amp; Chilli –</span><span class="price">$16.90</span></div><span class="desc">Soy squid lightly dressed with salt, chilli and onions</span></li>
    <li class="menu-item"><div class="row"><span>Fried Crab with Spicy Salt &amp; Chilli – Cua Muoi</span><span class="price">$16.90</span></div><span class="desc">Mushroom lightly dressed with salt, chilli and capsicum</span></li>
    <li class="menu-item"><div class="row"><span>Eggplant in Claypot Sensation – Ca Tim</span><span class="price">$13.90</span></div><span class="desc">A combination of onions and mushroom stirred with eggplant</span></li>
    <li class="menu-item"><div class="row"><span>Roast Soy Duck – Vit Quay</span><span class="price">$15.90</span></div></li>
    <li class="menu-item"><div class="row"><span>Soy Duck in Plum Sauce – Vit Xi Muoi</span><span class="price">$15.90</span></div></li>
    <li class="menu-item"><div class="row"><span>Roast Soy Pork – Xa Xiu</span><span class="price">$15.90</span></div></li>
    <li class="menu-item"><div class="row"><span>Mongolian Soy Lamb – Truu Nuong Mong Co</span><span class="price">$15.90</span></div></li>
    <li class="menu-item"><div class="row"><span>Mei Tan Eight Treasure – Bat Buu</span><span class="price">$16.90</span></div><span class="desc">A special stir fry with a combination of soy meats, tofu and vegetables</span></li>
    <li class="menu-item"><div class="row"><span>Grilled Soy Fish Sensation – Ca Nuong Trui</span><span class="price">$40.00</span></div><span class="desc">Served with rice paper, vermicelli and savoury dipping sauce</span></li>
    <li class="menu-item"><div class="row"><span>Small Vietnamese Fondue – Lau Thap Cam Nho</span><span class="price">$45.00</span></div><span class="desc">Vietnamese clear soup with soy meats, vermicelli and vegetables</span></li>
    <li class="menu-item"><div class="row"><span>Large Vietnamese Fondue – Lau Thap Cam Lon</span><span class="price">$60.00</span></div><span class="desc">Vietnamese clear soup with soy meats, vermicelli and vegetables</span></li>
  </ul>
</section>

</body>
</html>
```